Laboratory and geotechnical service provider needs Word template

We require a new Word Template for our business. We are looking for a modern, business-like format. We typically generate reports such as management plans, business plans, method statements, technical reports. These reports cover generally between 5 and 30 pages, but sometimes up to 500 pages including the appendices.

Lab reports have their own formats and are not parts of this scope.

Target Market(s)

We report to Clients such as construction industry contractors, governmental departments and engineering consultants.

Industry/Entity Type

Technical Service

Colors

Designer to choose colors to be used in the design.

Requirements
Must have
• The report needs a fancy cover page with a title field, subtitle, project field, client name field, reference number field. Photo/graphics as background on cover. Second page needs a revision table for document control. Table of contents up to 2 levels. Appendices to be part of TOC. Report first page with custom headings for body text, titles, subtitles, headings 1, 2, 3, etc. Include a table with caption, figure with caption, bullet list, numbered list. Appendix page. Please use fonts consistently, choose a common, but professional, modern font.
Nice to have
• We traditionally use black and yellow as company colours. Please visit our company page www.harbentestworks.com.
Should not have
• The two attached word documents is what we use now for your information, we are looking for something better!

```html
<!DOCTYPE html>
<html lang="en">
<head>
<meta charset="utf-8">
<title>Harben Testworks – Report Template</title>
<link href="https://fonts.googleapis.com/css2?family=Fira+Sans:wght@400;700&family=Source+Sans+3:wght@400;600&display=swap" rel="stylesheet">
<style>
:root{
  --bg:#ffcd1c;
  --yellow:#ffcf00;
  --black:#000;
  --gray:#58585a;
  --gray-light:#c8c8c8;
  --ink:#444;
  --white:#fff;
}
*{margin:0;padding:0;box-sizing:border-box}
html,body{width:1200px;height:849px;overflow:hidden;background:var(--bg)}
body{position:relative;font-family:"Fira Sans",sans-serif;color:var(--black)}

.brand{position:absolute;left:64px;top:20px;display:flex;align-items:center;gap:10px}
.brand-mark{width:20px;height:20px;background:var(--black)}
.brand-name{font-family:"Source Sans 3",sans-serif;font-size:21px;font-weight:400}

.page{position:absolute;width:229px;height:323px;background:var(--white);box-shadow:0 1px 3px rgba(0,0,0,.25);overflow:hidden}
.page > *{position:absolute}
.row1{top:97px}.row2{top:473px}
.col1{left:64px}.col2{left:345px}.col3{left:627px}.col4{left:908px}

.label{position:absolute;width:229px;text-align:center;font-family:"Source Sans 3",sans-serif;font-size:12.5px}

.page-head{left:0;top:0;width:229px;height:27px;background:var(--yellow);border-bottom:1.5px solid var(--black)}
.page-head .co{position:absolute;left:11px;top:15px;font-family:"Source Sans 3",sans-serif;font-size:4.2px}
.page-head .mark{position:absolute;right:11px;top:13px;font-size:5px;font-weight:700}
.page-foot{left:0;top:303px;width:229px;height:1.5px;background:var(--yellow)}
.page-num{right:23px;top:309px;font-size:4px}

.txt{font-size:4.1px;line-height:7px;color:var(--ink)}
.band{left:0;width:229px;height:9px;background:var(--yellow);font-size:5.6px;font-weight:700;line-height:9px;padding-left:22px}

/* cover */
.cover-photo{left:0;top:0;width:229px;height:201px;background:linear-gradient(180deg,#c9a200 0%,#e7bd10 40%,#ffcf00 75%)}
.cover-tile{top:124px;width:67px;height:67px;border:1.2px solid var(--black)}
.cover-tile.photo{background:linear-gradient(160deg,#9c7e10,#e0b510 60%,#f4c80c)}
.cover-tile.name{background:var(--yellow);display:flex;align-items:center;justify-content:center;font-size:9px;font-weight:700}
.cover-band{left:0;top:201px;width:229px;height:37px;background:var(--black);color:var(--yellow);padding:3px 0 0 18px}
.cover-band .t{font-size:8px;line-height:10.5px}
.cover-band .s{font-size:6px;line-height:10px}
.cover-project{left:18px;top:244px;font-size:9px}
.cover-ref{left:18px;top:257px;font-size:5px;color:#555}
.cover-client{left:18px;top:276px;font-size:7.5px;color:#444}
.cover-contact{left:18px;top:296px;font-size:4.5px;line-height:6.5px;color:#333}

/* tables */
table{border-collapse:collapse;font-size:3.9px}
td,th{height:8.5px;padding:0 1.5px;border:.4px solid #888}
th{background:var(--gray);color:var(--white);font-weight:400}
.rev{left:22px;top:34px;width:184px}
.rev td{text-align:center}
.rev tr.gap td{border:none;height:3px}
.copy{left:130px;top:78px;width:76px;background:var(--gray-light);font-size:4px;line-height:8.5px;padding-left:1.5px}

.toc{left:22px;top:49px;width:184px;font-size:4.1px;line-height:7px;color:#555}
.toc div{display:flex;justify-content:space-between}
.toc .sub{padding-left:14px}
.toc .gap{height:7px}

.h2{left:22px;top:53px;font-size:5.3px;color:#444}
.h3{left:22px;top:67px;font-size:4.5px;color:#555}
.ptitle{left:22px;top:81px;font-size:4.3px;color:#555}
.para4{left:22px;top:94px;width:184px}
.tbl1{left:22px;top:177px;width:184px}
.tbl1 td{text-align:left}
.tbl1 .sum td{background:var(--gray-light)}
.tbl1 .blank td{border:none;height:4px;background:none}
.caption{left:22px;font-size:2.8px;font-style:italic;color:#777}
.tbl2{left:22px;top:246px;width:102px}
.tbl2 td.k{background:var(--gray);color:var(--white)}
.tbl2 td.c{text-align:center}
.tbl2 .tot td{background:var(--gray-light);border:.4px solid #888;text-align:center}
.tbl2 .blank td{border:none;height:3.5px}

.image{left:0;top:133px;width:229px;height:128px;background:linear-gradient(180deg,#eef0f1 0%,#cdd4da 45%,#8d98a4 80%,#56606c 100%)}
.image-note{left:0;top:243px;width:229px;height:12px;background:rgba(0,0,0,.75);color:var(--yellow);font-family:"Source Sans 3",sans-serif;font-size:5.6px;line-height:12px;text-align:center}

.list-title{font-size:4.6px;color:#444}

.fonts-h{left:908px;top:540px;font-size:20px;font-weight:700;position:absolute}
.font-reg{position:absolute;left:908px;top:584px;font-size:15.5px}
.font-bold{position:absolute;left:908px;top:603px;font-size:15.5px;font-weight:700}
.colors-h{left:908px;top:658px;font-size:20px;font-weight:700;position:absolute}
.swatch{position:absolute;top:702px;width:51px;height:51px;border:3.5px solid var(--white)}
.swatch-label{position:absolute;top:755px;width:60px;text-align:center;font-family:"Source Sans 3",sans-serif;font-size:11px;line-height:12.5px}
</style>
</head>
<body>

<div class="brand"><span class="brand-mark"></span><span class="brand-name">Harben Testworks Co. WLL</span></div>

<!-- Cover -->
<section class="page row1 col1">
  <div class="cover-photo" role="img" aria-label="Yellow-toned photo of laboratory sample shelves"></div>
  <div class="cover-tile photo" style="left:11px" role="img" aria-label="Yellow-toned photo of a microscope at work"></div>
  <div class="cover-tile name" style="left:81px">Harben</div>
  <div class="cover-tile photo" style="left:151px" role="img" aria-label="Yellow-toned photo of a drilling rig on site"></div>
  <div class="cover-band"><div class="t">Document Title – Line 1</div><div class="t">Document Title – Line 2</div><div class="s">Subtitle</div></div>
  <div class="cover-project">Project Title</div>
  <div class="cover-ref">Reference number</div>
  <div class="cover-client">Clients Name</div>
  <div class="cover-contact">☎&nbsp; +974 4410 2286<br>@&nbsp; office@harbentestworks.com<br>■&nbsp; www.harbentestworks.com</div>
</section>
<div class="label col1" style="top:421px">Cover page</div>

<!-- Revision -->
<section class="page row1 col2">
  <div class="page-head"><span class="co">Harben Testworks Co. WLL</span><span class="mark">Harben</span></div>
  <table class="rev">
    <tr><th style="width:10px">Rev</th><th style="width:27px">Date</th><th>Details</th><th style="width:25px">Prepared</th><th style="width:25px">Checked</th><th style="width:27px">Approved</th></tr>
    <tr class="gap"><td colspan="6"></td></tr>
    <tr><td>1</td><td>03.12.2019</td><td>1<sup>st</sup> draft</td><td>RSV</td><td>TV</td><td>AJS</td></tr>
    <tr><td>2</td><td>04.12.2019</td><td>2<sup>nd</sup> draft</td><td>RSV</td><td>TV</td><td>AJS</td></tr>
    <tr><td>3</td><td>05.12.2019</td><td>1<sup>st</sup> Issue</td><td>RSV</td><td>TV</td><td>AJS</td></tr>
  </table>
  <div class="copy">Copy no.: &nbsp;1 / 5<br>Controlled Copy: &nbsp;&nbsp;YES</div>
  <div class="page-foot"></div><div class="page-num">2</div>
</section>
<div class="label col2" style="top:421px">Revision list</div>

<!-- TOC -->
<section class="page row1 col3">
  <div class="page-head"><span class="co">Harben Testworks Co. WLL</span><span class="mark">Harben</span></div>
  <div class="band" style="top:33px">Table of contents</div>
  <div class="toc">
    <div><span>1 Introduction</span><span>3</span></div>
    <div><span>2 Project overview</span><span>4</span></div>
    <div class="sub"><span>2.1 Under segment 1</span><span>4</span></div>
    <div class="sub"><span>2.2 Under segment 2</span><span>5</span></div>
    <div class="sub"><span>2.3 Under segment 3</span><span>6</span></div>
    <div><span>3 Technical requirements</span><span>8</span></div>
    <div class="sub"><span>3.1 Under segment 1</span><span>11</span></div>
    <div class="sub"><span>3.2 Under segment 2</span><span>13</span></div>
    <div class="sub"><span>3.3 Under segment 3</span><span>15</span></div>
    <div class="sub"><span>3.4 Under segment 4</span><span>18</span></div>
    <div class="sub"><span>3.5 Under segment 5</span><span>23</span></div>
    <div class="sub"><span>3.6 Under segment 6</span><span>29</span></div>
    <div><span>4 Business Management Requirement</span><span>32</span></div>
    <div class="sub"><span>4.1 Under segment 1</span><span>31</span></div>
    <div class="sub"><span>4.2 Under segment 2</span><span>38</span></div>
    <div class="sub"><span>4.3 Under segment 3</span><span>41</span></div>
    <div class="gap"></div>
    <div><span>Appendix A</span><span>42</span></div>
    <div class="sub"><span>Appendix A – Undersegment 1</span><span>43</span></div>
    <div><span>Appendix B</span><span>44</span></div>
    <div><span>Appendix C</span><span>48</span></div>
  </div>
  <div class="page-foot"></div><div class="page-num">3</div>
</section>
<div class="label col3" style="top:421px">Table of contents</div>

<!-- Headings -->
<section class="page row1 col4">
  <div class="page-head"><span class="co">Harben Testworks Co. WLL</span><span class="mark">Harben</span></div>
  <div class="band" style="top:36px">1. Heading 1</div>
  <div class="h2">1.1 Heading 2</div>
  <div class="h3">1.11 Heading 3</div>
  <div class="ptitle">Paragraph</div>
  <p class="txt para4">At vero eos et accusamus et iusto odio dignissimos ducimus qui blanditiis praesentium voluptatum deleniti atque corrupti quos dolores et quas molestias excepturi sint occaecati cupiditate non provident, similique sunt in culpa qui officia deserunt mollitia animi, id est laborum et dolorum fuga. Et harum quidem rerum facilis est et expedita distinctio. Possimus, omnis voluptas assumenda est, omnis dolor repellendus. Temporibus autem quibusdam et aut officiis debitis aut rerum necessitatibus saepe eveniet ut et voluptates repudiandae sint et molestiae non recusandae. Itaque earum rerum hic tenetur a sapiente delectus, ut aut reiciendis voluptatibus maiores alias consequatur aut perferendis doloribus asperiores repellat.</p>
  <table class="tbl1">
    <tr><th style="width:9px">No.</th><th style="text-align:left">Title 1</th><th style="width:25px;text-align:left">Title 2</th><th style="width:24px;text-align:left">Title 3</th><th style="width:59px;text-align:left">Title 4</th></tr>
    <tr><td style="text-align:center">1</td><td>Content</td><td>Content</td><td>Content</td><td>Content</td></tr>
    <tr><td style="text-align:center">2</td><td>Content</td><td>Content</td><td>Content</td><td>Content</td></tr>
    <tr><td style="text-align:center">3</td><td>Content</td><td>Content</td><td>Content</td><td>Content</td></tr>
    <tr class="sum"><td style="background:none"></td><td>Conclusion / Total / Sum</td><td></td><td>Pre Total</td><td>Total sum</td></tr>
    <tr class="blank"><td colspan="5"></td></tr>
    <tr><td style="border:none"></td><td style="border:none"></td><td style="border:none"></td><td style="border:none"></td><td style="background:var(--gray-light)">Total sum</td></tr>
  </table>
  <div class="caption" style="top:236px">Caption text for table style 1</div>
  <table class="tbl2">
    <tr><td class="k" style="width:56px">List item 1</td><td class="c">Text 01</td><td class="c">01</td></tr>
    <tr><td class="k">List item 2</td><td class="c">Text 02</td><td class="c">02</td></tr>
    <tr><td class="k">List item 3</td><td class="c">Text 03</td><td class="c">03</td></tr>
    <tr><td class="k">List item 4</td><td class="c">Text 04</td><td class="c">04</td></tr>
    <tr class="blank"><td colspan="3"></td></tr>
    <tr class="tot"><td style="border:none;background:none"></td><td>Total</td><td>Value</td></tr>
  </table>
  <div class="caption" style="top:295px">Caption text for table style 2</div>
  <div class="page-foot"></div><div class="page-num">4</div>
</section>
<div class="label col4" style="top:421px">Headings + Paragraph + Tables</div>

<!-- Paragraph & image -->
<section class="page row2 col1">
  <div class="page-head"><span class="co">Harben Testworks Co. WLL</span><span class="mark">Harben</span></div>
  <p class="txt" style="left:22px;top:34px;width:184px">Nam aliquet bibendum elit, ac imperdiet leo tristique sit amet. Pellentesque habitant morbi tristique senectus et netus et malesuada fames ac turpis egestas. Duis non scelerisque nunc. Donec luctus sollicitudin libero, eu condimentum ex tempor sit amet. Phasellus vel fringilla dui.</p>
  <p class="txt" style="left:22px;top:69px;width:184px">&nbsp;&nbsp;&nbsp;&nbsp;&nbsp;Vivamus a dapibus neque. Interdum et malesuada fames ac ante ipsum primis in faucibus. Fusce quis viverra ligula, a egestas elit. Integer ut luctus lacus. Nunc et pretium sem. Nulla varius lacus et ligula sollicitudin, vel tempor urna tincidunt. Nam et nulla pretium, rutrum mi nec, laoreet odio. Fusce scelerisque malesuada odio, et auctor enim lacinia vel. Maecenas quis augue id erat cursus lacinia vel ut lectus. In elementum efficitur libero, a eleifend mauris dictum eget. Sed ut varius lacus, vitae pulvinar metus. Nullam eu turpis sit amet augue volutpat faucibus. Etiam ac risus sed erat porttitor interdum a nec turpis.</p>
  <div class="image" role="img" aria-label="Photo of a bright testing laboratory with staff in yellow coats at workbenches"></div>
  <div class="image-note">← Images if possible should always be from edge to edge. →</div>
  <div class="caption" style="top:263px">Caption text for Figure style 1</div>
  <p class="txt" style="left:22px;top:271px;width:184px">Sed quia non numquam eius modi tempora incidunt ut labore et dolore magnam aliquam quaerat voluptatem. Ut enim ad minima veniam, quis nostrum exercitationem ullam corporis suscipit laboriosam, nisi ut aliquid ex ea commodi consequatur? Quis autem vel eum iure reprehenderit qui in ea voluptate velit esse</p>
  <div class="page-foot"></div><div class="page-num">5</div>
</section>
<div class="label col1" style="top:797px">Parapgraph &amp; Image</div>

<!-- Lists -->
<section class="page row2 col2">
  <div class="page-head"><span class="co">Harben Testworks Co. WLL</span><span class="mark">Harben</span></div>
  <p class="txt" style="left:22px;top:34px;width:184px">quam nihil molestiae consequatur, vel illum qui dolorem eum fugiat quo voluptas nulla pariatur?</p>
  <p class="txt" style="left:22px;top:59px;width:184px">Nullam fermentum, dolor quis iaculis maximus, sem erat auctor orci, a dignissim arcu nisi quis nunc. Sed eu sem at velit tempor finibus eget non felis. Vivamus lacus dolor, porta vitae orci vitae, auctor commodo nisl. Vestibulum luctus odio ex, nec pulvinar orci tincidunt at. Suspendisse potenti. Curabitur ornare nibh porttitor augue porta, eget consequat augue cursus. Nam volutpat nisl at justo dignissim imperdiet.</p>
  <div class="txt" style="left:22px;top:111px;width:184px">
    <div class="list-title">List with munbers:</div>
    1 Text enumeration<br>2 Text enumeration<br>3 Text enumeration<br>4 Text enumeration<br>5 Text enumeration<br>6 Text enumeration<br>
    <span style="padding-left:14px">6.1 Subnumeration if needed</span><br><span style="padding-left:14px">6.2 Subnumeration if needed</span><br>
    7 Text enumeration<br>8 Text enumeration<br>9 Text enumeration<br>10 Text enumeration<br>11 Text enumeration<br>12 Text enumeration
  </div>
  <p class="txt" style="left:22px;top:226px;width:184px">Mauris et turpis molestie, tempus sem vel, pretium justo. Vivamus urna erat, pulvinar fringilla est ac, fringilla ullamcorper sem. Curabitur venenatis sit amet</p>
  <div class="txt" style="left:22px;top:248px;width:184px">
    <div class="list-title">List with bullets:</div>
    ▪ Bullet text<br>▪ Bullet text<br>▪ Bullet text<br>▪ Bullet text<br>▪ Bullet text<br>▪ Bullet text
  </div>
  <div class="page-foot"></div><div class="page-num">6</div>
</section>
<div class="label col2" style="top:797px">Numbered &amp; Bulleted lists</div>

<!-- Appendix -->
<section class="page row2 col3">
  <div class="page-head"><span class="co">Harben Testworks Co. WLL</span><span class="mark">Harben</span></div>
  <div class="band" style="top:39px">Appendix</div>
  <p class="txt" style="left:22px;top:57px;width:184px;line-height:8.1px">Nunc in vulputate magna. Donec quis libero ut massa vulputate bibendum. Curabitur sodales, quam in vestibulum consectetur, ex neque varius elit, eget viverra nunc metus nec sem. Praesent semper nec magna dignissim tempor. Etiam vitae vehicula tellus. Nullam augue ligula, elementum non tellus ut, vestibulum imperdiet justo. Fusce sed nisl cursus, ultrices arcu eget, sagittis ante. Donec ultricies venenatis elementum. Nemo enim ipsam voluptatem quia voluptas sit aspernatur aut odit aut fugit, sed quia consequuntur magni dolores eos qui ratione voluptatem sequi nesciunt. Neque porro quisquam est, qui dolorem ipsum quia dolor sit amet, consectetur, adipisci velit, sed quia non numquam eius modi tempora incidunt ut labore et dolore magnam aliquam quaerat voluptatem. Ut enim ad minima veniam, quis nostrum exercitationem ullam corporis suscipit laboriosam, nisi ut aliquid ex ea commodi consequatur?</p>
  <div class="page-foot"></div><div class="page-num">7</div>
</section>
<div class="label col3" style="top:797px">Appendix page</div>

<!-- Specs -->
<div class="fonts-h">Fonts used :</div>
<div class="font-reg">Lucida Sans - Regular</div>
<div class="font-bold">Lucida Sans - Bold</div>
<div class="colors-h">Colors used :</div>
<div class="swatch" style="left:908px;background:var(--black)"></div>
<div class="swatch" style="left:967px;background:var(--gray)"></div>
<div class="swatch" style="left:1025px;background:var(--yellow)"></div>
<div class="swatch-label" style="left:904px">Black</div>
<div class="swatch-label" style="left:963px">Dark gray 1</div>
<div class="swatch-label" style="left:1021px">Yellow<br>#FFCF00</div>

</body>
</html>
```